TRNV LLP website - revamping our website after 23 years

Our website needs a complete overhaul. The purpose of this exercise is to provide us with your vision of what you think the website should look like. We don't need the website to be created or coded. Just need creative designs.

We have a four sites that we would like to base our website on;

We like the simplicity of Fairwicks, the style of Pemberly Strand and Kettridge.

http://www.pemberlystrand-example.com/en/toronto-ontario/
http://www.fairwicks-example.ca/
hallkettridge-example.com
http://www.vendrupe-example.com/our-professionals.html

We have a logo that we would like to use which will be attached below. We need to keep our website looking very professional as we have a large number of high net worth clients.
Updates

Hi, We've received some good website designs but they appear to be the same type of template websites we've received in the past - this is not what we're looking for. What we want is a unique website that is modelled on the following three company websites: http://www.fairwicks-example.ca/ www.hallkettridge-example.com/ http://www.pemberlystrand-example.com/en/toronto-ontario/

Thank you everyone for your designs. I will be posting updates and my comments on the various designs in the next day - I want to thank you for the creative designs I see. I thought i would explain a bit about our firm and perhaps it can help when you design the theme of our website: - Our firm is like a family and our clients are truly like our friends. We have close knit relationships in and outside of the office with staff and clients. - We are an 'out of the box' type of firm. We operate differently than most firms and that's a differentiating factor in what makes us who we are - Our slogan is "Count on us" which is a testament to the way we run our practice - We would like an open, fresh, clean look to our website - we don't want the landing page to be overly long or complex because we have limited time to update the website and limited content That's it for the time being - when things come to mind I will post them here.

Can we try a design as follows: - make the website look very similar to www.fairwicks-example.ca - use the same background colour - Keep the same black top but insert our logo - incorporate some of the content from our current website www.trnv-example.com

I have been away dealing with a personal matter. I will look into these websites tomorrow afternoon and provide more feedback / info on the top designer. Thank you

Hi designers, I want to apologize for the delay. I plan on wrapping things up within the next few days. I will go through a few of the top designs and offer my comments. Thank you for your patience.

Target Market(s)

Mainly our current clients - We have a large number of high net worth individuals as clients.

Industry/Entity Type

Accounting

Number of Pages Required

1 page

Requirements
Must have
• Please model website on the websites indicated above.
• Our current website is www.trnv-example.com. It's dark, cluttered and not inviting. We want a fresh, clean website. Please incorporate the logo's attached below.

```html
<!DOCTYPE html>
<html lang="en">
<head>
<meta charset="utf-8">
<title>TRNV LLP — Chartered Professional Accountants</title>
<link href="https://fonts.googleapis.com/css2?family=Cinzel:wght@400;600;700&family=Merriweather:wght@700;900&family=Lato:ital,wght@0,400;0,700;1,400&display=swap" rel="stylesheet">
<style>
  :root{
    --charcoal:#373738;
    --charcoal-dark:#2c2c2d;
    --accent:#1ba1dc;
    --ink:#1d1d1d;
    --body-text:#5a5a5a;
    --rule:#b9b9b9;
    --field-border:#b5b5b5;
    --white:#ffffff;
  }
  *{box-sizing:border-box;margin:0;padding:0}
  html,body{width:1200px;height:1048px;overflow:hidden}
  body{position:relative;background:var(--white);font-family:'Lato',sans-serif;color:var(--body-text)}

  /* Header */
  .site-header{position:absolute;left:0;top:0;width:1200px;height:141px;background:var(--charcoal)}
  .brand{position:absolute;left:131px;top:84px;display:flex;align-items:center;gap:10px}
  .brand-mark{width:22px;height:22px;background:var(--accent)}
  .brand-name{font-family:'Cinzel',serif;font-weight:400;font-size:36px;color:var(--white);letter-spacing:1px;line-height:1}
  .contact-email{position:absolute;right:378px;top:5px;display:flex;align-items:center;gap:8px;font-size:15px;color:var(--white);white-space:nowrap}
  .contact-phone{position:absolute;left:834px;top:0;width:235px;height:31px;background:var(--accent);
    clip-path:polygon(0 0,100% 0,93% 100%,7% 100%);display:flex;align-items:center;justify-content:center;gap:6px;
    font-size:20px;color:var(--white)}
  .main-nav{position:absolute;left:419px;top:89px;width:644px;display:flex;justify-content:space-between}
  .main-nav a{font-family:'Cinzel',serif;font-weight:600;font-size:16px;text-transform:uppercase;color:var(--white);
    text-decoration:none;height:32px;line-height:32px;white-space:nowrap}
  .main-nav a.is-active{background:var(--accent);width:75px;text-align:center}

  /* Hero */
  .hero{position:absolute;left:0;top:141px;width:1200px;height:454px;
    background:linear-gradient(100deg,#c9d3da 0%,#e9eef2 22%,#b9cde0 45%,#a9c4e0 60%,#d9e2ea 80%,#c4ccd3 100%);
    border-bottom:4px solid var(--charcoal-dark)}
  .hero-tagline{position:absolute;left:0;width:1200px;top:188px;text-align:center;font-family:'Merriweather',serif;
    font-weight:900;color:var(--white);text-shadow:1px 2px 3px rgba(0,0,0,.55);line-height:33px}
  .hero-tagline .line-one{font-size:23px}
  .hero-tagline .line-one strong{font-size:28px}
  .hero-tagline .line-two{font-size:23px}
  .hero-arrow{position:absolute;top:197px;width:46px;height:46px;border-radius:50%;background:rgba(55,55,55,.75)}
  .hero-arrow.prev{left:38px}
  .hero-arrow.next{left:1116px;background:rgba(75,75,75,.85)}
  .hero-arrow svg{position:absolute;left:13px;top:11px}

  /* Content columns */
  .panel{position:absolute;top:617px}
  .panel-head{display:flex;align-items:center;height:60px;border-bottom:1px dashed var(--rule);padding-bottom:4px}
  .diamond{width:60px;height:60px;position:relative;flex:none}
  .diamond::before{content:"";position:absolute;left:10px;top:10px;width:40px;height:40px;background:var(--accent);transform:rotate(45deg)}
  .diamond svg{position:absolute;left:18px;top:18px}
  .panel-title{font-family:'Cinzel',serif;font-weight:700;font-size:23px;text-transform:uppercase;color:var(--ink);margin-left:12px;white-space:nowrap}
  .panel-photo{margin-top:9px;width:272px;height:125px;border:1px solid #ccc}
  .panel-copy{margin-top:20px;width:276px;font-size:13.6px;line-height:21px;padding-left:2px}
  .read-more{display:block;text-align:right;width:256px;margin-top:-10px;font-weight:700;font-size:14.5px;color:var(--accent);text-decoration:none}
  .panel.who{left:131px;width:276px}
  .panel.services{left:464px;width:276px}
  .panel.inquiry{left:788px;width:278px}
  .panel.who .panel-head,.panel.services .panel-head{width:272px}
  .photo-office{background:linear-gradient(90deg,#cfd6dc 0%,#e4e7ea 40%,#3b3f48 55%,#d7dce1 80%,#bfc5cb 100%)}
  .photo-team{background:linear-gradient(90deg,#9db4cc 0%,#d3dde6 35%,#8ea7c0 60%,#dde4ea 100%)}
  .column-divider{position:absolute;top:720px;width:1px;height:190px;background:linear-gradient(#fff,#e2e2e2,#fff)}

  .inquiry-form{margin-top:14px;margin-left:10px}
  .field{display:block;width:267px;height:28px;border:1px solid var(--field-border);border-radius:2px;margin-bottom:13px;
    font-family:'Lato',sans-serif;font-style:italic;font-size:13.5px;color:#666;padding:5px 9px;background:var(--white);resize:none}
  .field.message{height:80px}
  .submit{display:block;width:84px;height:32px;border:0;border-radius:2px;background:var(--accent);color:var(--white);
    font-family:'Lato',sans-serif;font-weight:700;font-size:18px;margin-top:-4px}

  /* Footer */
  .site-footer{position:absolute;left:0;top:1001px;width:1200px;height:47px;background:var(--charcoal)}
  .copyright{position:absolute;left:133px;top:14px;font-size:14.5px;color:var(--white)}
  .social{position:absolute;left:936px;top:11px;display:flex;gap:6px}
  .social span{width:26px;height:26px;border-radius:50%;background:#e9e9e9}
</style>
</head>
<body>

<header class="site-header">
  <div class="brand">
    <span class="brand-mark"></span>
    <span class="brand-name">TRNV LLP</span>
  </div>
  <div class="contact-email">
    <svg width="18" height="14" viewBox="0 0 18 14" aria-hidden="true"><rect x="1" y="3" width="16" height="10" fill="#fff"/><path d="M1 3 L9 9 L17 3" stroke="#373738" stroke-width="1.4" fill="none"/></svg>
    <span>info@trnv-example.com</span>
  </div>
  <div class="contact-phone">
    <svg width="18" height="18" viewBox="0 0 18 18" aria-hidden="true"><circle cx="9" cy="9" r="8" stroke="#fff" stroke-width="1.5" fill="none"/><path d="M6 5 L7.5 5 L8 7.3 L7 8 C7.6 9.4 8.6 10.4 10 11 L10.7 10 L13 10.5 L13 12 C9 12.5 5.5 9 6 5Z" fill="#fff"/></svg>
    <span>123-456-7890</span>
  </div>
  <nav class="main-nav">
    <a href="#" class="is-active">Home</a>
    <a href="#">About Us</a>
    <a href="#">Services</a>
    <a href="#">Library</a>
    <a href="#">Links</a>
    <a href="#">Careers</a>
    <a href="#">Contact Us</a>
  </nav>
</header>

<section class="hero" role="img" aria-label="Photo of hands holding a tablet showing bar and pie charts over printed financial tables">
  <div class="hero-tagline">
    <div class="line-one">We Bring Over <strong>100 YEARS</strong> Of</div>
    <div class="line-two">Valuable Experience To The Practice Of Public Accounting</div>
  </div>
  <span class="hero-arrow prev"><svg width="20" height="24" viewBox="0 0 20 24" aria-hidden="true"><path d="M14 2 L5 12 L14 22" stroke="#bbb" stroke-width="2.5" fill="none"/></svg></span>
  <span class="hero-arrow next"><svg width="20" height="24" viewBox="0 0 20 24" aria-hidden="true"><path d="M6 2 L15 12 L6 22" stroke="#fff" stroke-width="2.5" fill="none"/></svg></span>
</section>

<section class="panel who">
  <div class="panel-head">
    <span class="diamond"><svg width="24" height="24" viewBox="0 0 24 24" aria-hidden="true"><circle cx="12" cy="7" r="4.5" fill="none" stroke="#fff" stroke-width="1.8"/><path d="M3 23 C3 15 21 15 21 23" fill="none" stroke="#fff" stroke-width="1.8"/></svg></span>
    <h2 class="panel-title">Who We Are</h2>
  </div>
  <div class="panel-photo photo-office" role="img" aria-label="Photo of a smiling accountant in a suit in a bright office"></div>
  <p class="panel-copy">Lorem ipsum dolor sit amet, consectetuer is adipiscing elit, sed diam nonummy nibh the euismod tincidunt ut laoreet Lorem ipsum a dolor sit amet, consectetuer adipiscing elit, sed diam .</p>
  <a href="#" class="read-more">Read More</a>
</section>

<span class="column-divider" style="left:433px"></span>
<span class="column-divider" style="left:759px"></span>

<section class="panel services">
  <div class="panel-head">
    <span class="diamond"><svg width="24" height="24" viewBox="0 0 24 24" aria-hidden="true"><path d="M1 9 L7 6 L12 9 L17 6 L23 9 L23 14 L17 18 L12 15 L7 18 L1 14 Z" fill="#fff"/></svg></span>
    <h2 class="panel-title">Services</h2>
  </div>
  <div class="panel-photo photo-team" role="img" aria-label="Photo of a smiling professional with colleagues meeting in the background"></div>
  <p class="panel-copy">Lorem ipsum dolor sit amet, consectetuer is adipiscing elit, sed diam nonummy nibh the euismod tincidunt ut laoreet Lorem ipsum a dolor sit amet, consectetuer adipiscing elit, sed diam .</p>
  <a href="#" class="read-more">Read More</a>
</section>

<section class="panel inquiry">
  <div class="panel-head">
    <span class="diamond"><svg width="24" height="24" viewBox="0 0 24 24" aria-hidden="true"><rect x="3" y="3" width="15" height="19" fill="none" stroke="#fff" stroke-width="1.8"/><path d="M6 8 H15 M6 12 H13 M6 16 H11" stroke="#fff" stroke-width="1.5"/><path d="M13 18 L21 8 L23 10 L15 20 Z" fill="#fff"/></svg></span>
    <h2 class="panel-title">Quick Inquiry</h2>
  </div>
  <form class="inquiry-form">
    <input class="field" type="text" placeholder="Name">
    <input class="field" type="email" placeholder="Email">
    <input class="field" type="tel" placeholder="Phone">
    <textarea class="field message" placeholder="Message"></textarea>
    <button class="submit" type="button">SUBMIT</button>
  </form>
</section>

<footer class="site-footer">
  <p class="copyright">© 2015&nbsp; TRNV LLP.&nbsp; All Rights Reserved</p>
  <div class="social" aria-label="Social links">
    <span></span><span></span><span></span><span></span>
  </div>
</footer>

</body>
</html>
```